MoveNest Landing Page

We need to freshen up our homepage.

The company is MoveNest.com. We provide cloud-based management software for class venues - dance, yoga, martial arts, etc.

The challenge here is to create something that's simultaneously lighthearted and professional. We want our customers to know that the software is easy, fun and non-intimidating, but also powerful enough to handle whatever they throw at it.

Page content can remain the same as it is now. Feel free to move things around, manipulate it however you like.

We like our logo, but feel free to manipulate it as part of your design. Fonts used in the logo are Futura Extra Bold and Rockwell.

NOTE: The default screenshot in the homepage video is NOT our branding choice, it just happens to be the default freeze frame from vidloop.. Feel free to ignore it altogether in your design. We are not affiliated with that character, or the app that we used to create the vid.
Updates

Project Deadline Extended
Reason: We are extending this contest by request. Out of 65 designs, so far we only really like 4. There's still a good chance to win this contract! Please submit your very best :) Owen

Target Market(s)

Studio owners who are not necessarily tech savvy.

Industry/Entity Type

Software

Requirements
Must have
• Look and feel of a modern web app.

Delivery in a layered PSD.

```html
<!DOCTYPE html>
<html lang="en">
<head>
<meta charset="utf-8">
<title>MoveNest – The easiest way to manage your classes</title>
<link href="https://fonts.googleapis.com/css2?family=Open+Sans:ital,wght@0,400;0,600;0,700;0,800;1,600&family=Roboto+Slab:wght@800;900&display=swap" rel="stylesheet">
<style>
  :root {
    --blue: #2563b4;
    --blue-deep: #1c4f96;
    --blue-ink: #17407d;
    --green: #79e00e;
    --green-deep: #5cbc05;
    --green-dark: #64c40a;
    --orange: #ff5a0a;
    --orange-deep: #d84400;
    --nav-grey: #6b6b6b;
    --title-blue: #5a7db0;
    --muted: #9a9a9a;
    --paper: #f6f6f6;
    --white: #ffffff;
  }
  * { box-sizing: border-box; margin: 0; padding: 0; }
  html, body { width: 1200px; height: 976px; overflow: hidden; }
  body { position: relative; background: var(--paper); font-family: "Open Sans", Arial, sans-serif; }

  .site-header { position: absolute; left: 0; top: 0; width: 1200px; height: 77px; background: var(--white); }
  .brand { position: absolute; left: 130px; top: 16px; font-family: "Open Sans", Arial, sans-serif; font-weight: 800; font-size: 34px; color: var(--blue); letter-spacing: -0.5px; }
  .main-nav { position: absolute; left: 625px; top: 26px; display: flex; gap: 28px; }
  .nav-link { display: flex; align-items: center; gap: 8px; color: var(--nav-grey); font-weight: 700; font-size: 16px; text-decoration: none; }
  .nav-link svg { width: 18px; height: 18px; fill: var(--title-blue); }
  .btn { position: absolute; display: flex; align-items: center; justify-content: center; gap: 6px; border-radius: 9px; color: var(--white); font-family: "Roboto Slab", Georgia, serif; font-weight: 800; text-decoration: none; }
  .btn-orange { background: var(--orange); box-shadow: 0 3px 0 var(--orange-deep); }
  .btn-green { background: var(--green); box-shadow: 0 3px 0 var(--green-deep); }
  .btn-get-started { left: 927px; top: 17px; width: 131px; height: 42px; font-size: 14px; }

  .hero { position: absolute; left: 0; top: 77px; width: 1200px; height: 443px; overflow: hidden; }
  .hero-bg { position: absolute; inset: 0; }
  .product-preview { position: absolute; left: 82px; top: 41px; width: 440px; height: 362px; border-radius: 12px; background: linear-gradient(180deg, #3a3a3a 0 72%, #e4e4e4 72% 84%, #bfc3c8 84%); }
  .hero-name { position: absolute; left: 548px; top: 65px; width: 222px; text-align: center; font-family: "Roboto Slab", Georgia, serif; font-weight: 900; font-size: 44px; color: var(--white); }
  .hero-title { position: absolute; left: 548px; top: 198px; width: 522px; text-align: center; color: var(--white); font-family: "Roboto Slab", Georgia, serif; font-weight: 900; text-transform: uppercase; line-height: 1; }
  .hero-title .line-1 { display: block; font-size: 55px; letter-spacing: 0.5px; }
  .hero-title .line-2 { display: block; font-size: 37px; margin-top: 2px; }
  .hero-title .line-3 { display: block; font-size: 30px; margin-top: 4px; }
  .hero-title small { font-size: 0.72em; }
  .cta { position: absolute; top: 336px; width: 220px; height: 64px; justify-content: flex-start; padding-left: 16px; gap: 14px; }
  .cta-video { left: 550px; }
  .cta-setup { left: 850px; }
  .cta svg { flex: none; }
  .cta-text { display: flex; flex-direction: column; align-items: center; line-height: 1.15; }
  .cta-main { font-size: 14px; text-transform: uppercase; }
  .cta-main b { font-size: 24px; font-weight: 800; }
  .cta-sub { font-family: "Open Sans", Arial, sans-serif; font-style: italic; font-weight: 600; font-size: 14px; }
  .cta-chevron { position: absolute; right: 10px; top: 24px; }

  .features { position: absolute; left: 122px; top: 568px; display: flex; }
  .feature { width: 160px; text-align: center; }
  .feature svg { width: 68px; height: 66px; stroke: var(--green); fill: none; stroke-width: 4; stroke-linecap: round; stroke-linejoin: round; }
  .feature-title { margin-top: 14px; color: var(--title-blue); font-weight: 600; font-size: 19px; text-transform: uppercase; }
  .feature-text { color: var(--muted); font-size: 14px; line-height: 16px; }
  .btn-learn { left: 523px; top: 720px; width: 152px; height: 47px; font-size: 14px; }

  .faq-card { position: absolute; top: 829px; width: 460px; height: 160px; border-radius: 6px; overflow: hidden; }
  .faq-question { left: 129px; background: var(--blue); }
  .faq-answer { left: 609px; background: var(--green); }
  .faq-letter { position: absolute; font-family: "Roboto Slab", Georgia, serif; font-weight: 900; font-size: 120px; line-height: 1; }
  .faq-question .faq-letter { left: 24px; top: 22px; color: var(--blue-ink); }
  .faq-answer .faq-letter { left: 24px; top: 44px; color: var(--green-dark); }
  .faq-heading { position: absolute; left: 128px; top: 30px; color: var(--white); font-family: "Roboto Slab", Georgia, serif; font-weight: 900; font-size: 44px; line-height: 46px; }
  .faq-body { position: absolute; left: 130px; top: 26px; width: 310px; color: var(--white); font-size: 14px; line-height: 17px; }
</style>
</head>
<body>
  <header class="site-header">
    <div class="brand">MoveNest</div>
    <nav class="main-nav">
      <a class="nav-link" href="#"><svg viewBox="0 0 20 20"><path d="M10 2 1 10h3v8h4.5v-5h3v5H16v-8h3z"/></svg>HOME</a>
      <a class="nav-link" href="#"><svg viewBox="0 0 20 20"><circle cx="6" cy="6" r="5"/><path d="M8 7l10 10-2 2-2-2-1 1-2-2 1-1-5-5z"/></svg>LOGIN</a>
      <a class="nav-link" href="#"><svg viewBox="0 0 20 20"><path fill-rule="evenodd" d="M10 1a9 9 0 1 1 0 18 9 9 0 0 1 0-18zm0 5a4 4 0 1 0 0 8 4 4 0 0 0 0-8z"/></svg>HELP</a>
    </nav>
    <a class="btn btn-orange btn-get-started" href="#">GET STARTED <svg width="8" height="12" viewBox="0 0 8 12"><path d="M1 1l5 5-5 5" stroke="#fff" stroke-width="2.5" fill="none"/></svg></a>
  </header>

  <section class="hero">
    <svg class="hero-bg" width="1200" height="443" viewBox="0 0 1200 443">
      <rect width="1200" height="443" fill="var(--blue)"/>
      <polygon points="0,360 1200,310 1200,443 0,443" fill="var(--blue-deep)"/>
      <ellipse cx="300" cy="397" rx="140" ry="26" fill="var(--blue-ink)"/>
    </svg>
    <div class="product-preview" role="img" aria-label="Desktop monitor showing the class calendar app with a class detail window open"></div>
    <div class="hero-name">MoveNest</div>
    <h1 class="hero-title">
      <span class="line-1">The easiest way</span>
      <span class="line-2"><small>to</small> manage your classes</span>
      <span class="line-3"><small>and</small> accept payments online</span>
    </h1>
    <a class="btn btn-green cta cta-video" href="#">
      <svg width="30" height="32" viewBox="0 0 30 32"><path d="M3 3l24 13-24 13z" stroke="#fff" stroke-width="2.5" fill="none" stroke-linejoin="round"/></svg>
      <span class="cta-text"><span class="cta-main"><b>1</b> minute video</span><span class="cta-sub">How it works</span></span>
      <svg class="cta-chevron" width="8" height="14" viewBox="0 0 8 14"><path d="M1 1l6 6-6 6" stroke="#fff" stroke-width="2.5" fill="none"/></svg>
    </a>
    <a class="btn btn-orange cta cta-setup" href="#">
      <svg width="34" height="36" viewBox="0 0 34 36"><path d="M2 34 22 14M24 2v6M30 8h-5M30 16l-4-3M17 5l4 4" stroke="#fff" stroke-width="2.5" fill="none" stroke-linecap="round"/></svg>
      <span class="cta-text"><span class="cta-main"><b>5</b> minute setup!</span><span class="cta-sub">It’s Free :)</span></span>
      <svg class="cta-chevron" width="8" height="14" viewBox="0 0 8 14"><path d="M1 1l6 6-6 6" stroke="#fff" stroke-width="2.5" fill="none"/></svg>
    </a>
  </section>

  <section class="features">
    <div class="feature">
      <svg viewBox="0 0 68 66"><rect x="4" y="10" width="60" height="38" rx="2"/><path d="M34 48v10M22 60h24"/></svg>
      <div class="feature-title">Web based</div><div class="feature-text">Logn anywhere</div>
    </div>
    <div class="feature">
      <svg viewBox="0 0 68 66"><path d="M58 8 10 30l22 4 4 22z"/></svg>
      <div class="feature-title">Intuitive</div><div class="feature-text">Easy to use</div>
    </div>
    <div class="feature">
      <svg viewBox="0 0 68 66"><path d="M58 4C40 6 28 18 22 38l8 8c20-6 32-18 34-36zM22 38l-10-2 8-12h12M30 46l2 10 12-8V36M18 50l-8 8M24 54l-4 4"/><circle cx="46" cy="20" r="5"/></svg>
      <div class="feature-title">Robust</div><div class="feature-text">Fast and powerful</div>
    </div>
    <div class="feature">
      <svg viewBox="0 0 68 66"><rect x="12" y="28" width="44" height="34" rx="3"/><path d="M20 28V18a14 14 0 0 1 28 0v10M34 40v10"/></svg>
      <div class="feature-title">Secure</div><div class="feature-text">Your info is super safe</div>
    </div>
    <div class="feature">
      <svg viewBox="0 0 68 66"><path d="M8 8h14M8 8v14M8 8l16 16M60 8H46M60 8v14M60 8 44 24M8 58h14M8 58V44M8 58l16-16M60 58H46M60 58V44M60 58 44 42"/></svg>
      <div class="feature-title">Versatile</div><div class="feature-text">Suitable for any<br>class venue</div>
    </div>
    <div class="feature">
      <svg viewBox="0 0 68 66"><rect x="6" y="20" width="56" height="14"/><rect x="10" y="34" width="48" height="28"/><path d="M34 20v42M34 20c-4-10-16-14-16-6s16 6 16 6c4-10 16-14 16-6s-16 6-16 6"/></svg>
      <div class="feature-title">Affordable</div><div class="feature-text">Free version!</div>
    </div>
  </section>

  <a class="btn btn-orange btn-learn" href="#">LEARN MORE <svg width="8" height="12" viewBox="0 0 8 12"><path d="M1 1l5 5-5 5" stroke="#fff" stroke-width="2.5" fill="none"/></svg></a>

  <article class="faq-card faq-question">
    <span class="faq-letter">Q</span>
    <h2 class="faq-heading">What is<br>MoveNest?</h2>
  </article>
  <article class="faq-card faq-answer">
    <span class="faq-letter">A</span>
    <p class="faq-body">MoveNest is the easiest and most affordable way to manage your class studio or venue. We help simplify your daily tasks by leveraging the power of the internet, saving you time and money. Anyone can learn to use MoveNest with our clean, common-sense website.</p>
  </article>
</body>
</html>
```